Landing Page Only for text marketing service pingrova.net

Our current site pingrova.net needs a custom landing page for paid advertisements that is conversion centered as well as clear and concise. We want to focus on displaying the information effectively without getting too wordy or confusing to gain a higher conversion rate as our main goal.

We want more emphasis on the Try for $1 that includes 500 messages and custom keyword. The offer has no commitments. Upgrade or cancel at anytime.

We also want the landing page to focus on the benefits and marketing advantages (found in benefits tab), possible uses: mobile coupons, reminders/alerts, contests, daily specials, etc. (more examples can be found in how it works tab), and how it works.

The landing page can link to other parts of the site or use any information from other parts of the site. Our logo is attached in files. We want the design to match the overall color scheme of the site.

Target Market(s)

US based customers, business owners.

Industry/Entity Type

Marketing

Coding

Coded - Design and coding required

Number of Pages Required

1 page

Requirements
Must have
• See project description.
Nice to have
• See project description and any additional ideas welcomed from the designer.

```html
<!DOCTYPE html>
<html lang="en">
<head>
<meta charset="utf-8">
<title>Pingrova – Try for $1</title>
<link href="https://fonts.googleapis.com/css2?family=Roboto:wght@400;500;700;900&family=Roboto+Condensed:wght@700&display=swap" rel="stylesheet">
<style>
  :root {
    --red: #d81f26;
    --red-dark: #b9161c;
    --ink: #2f2f2f;
    --white: #ffffff;
    --band: #e5e5e5;
    --ring: rgba(255,255,255,0.45);
  }
  * { box-sizing: border-box; margin: 0; padding: 0; }
  html, body { width: 1200px; height: 825px; overflow: hidden; background: var(--white); }
  body { position: relative; font-family: "Roboto", Arial, sans-serif; color: var(--ink); }

  .site-header { position: absolute; left: 0; top: 0; width: 1200px; height: 78px; background: var(--white); }
  .brand { position: absolute; left: 162px; top: 24px; display: flex; align-items: center; gap: 8px;
    font-weight: 700; font-size: 22px; color: var(--ink); }
  .brand-dot { width: 14px; height: 14px; border-radius: 50%; background: var(--red); }
  .benefit-nav { position: absolute; top: 9px; left: 0; width: 1200px; }
  .benefit { position: absolute; width: 180px; margin-left: -90px; text-align: center;
    font-family: "Roboto Condensed", Arial, sans-serif; font-weight: 700; font-size: 15px; color: var(--ink); }
  .benefit svg { display: block; margin: 0 auto 3px; width: 34px; height: 32px; }

  .hero { position: absolute; left: 0; top: 78px; width: 1200px; height: 526px; overflow: hidden;
    background: radial-gradient(ellipse at 80% 38%, #f3e6cf 0%, rgba(243,230,207,0) 28%),
                radial-gradient(ellipse at 10% 20%, #e9d6c0 0%, rgba(233,214,192,0) 25%),
                linear-gradient(180deg, #c9d4de 0%, #8fa3b7 45%, #6f8599 100%); }
  .hero-photo { position: absolute; left: 560px; top: 20px; width: 640px; height: 506px;
    background: radial-gradient(ellipse at 45% 60%, #e3b69d 0%, #d9a58a 35%, rgba(200,150,125,0) 70%); }

  .offer { position: absolute; border-radius: 50%; background: var(--white); display: flex;
    flex-direction: column; align-items: center; justify-content: center; text-align: center;
    box-shadow: 0 0 0 9px var(--ring); color: var(--ink); line-height: 1; }
  .offer-count { left: 245px; top: 27px; width: 168px; height: 168px; }
  .offer-count .big { font-weight: 900; font-size: 64px; letter-spacing: -1px; }
  .offer-count .small { font-weight: 700; font-size: 19px; margin-top: -2px; }
  .offer-keyword { left: 414px; top: 150px; width: 136px; height: 136px; }
  .offer-keyword .big { font-weight: 700; font-size: 26px; }
  .offer-keyword .small { font-weight: 400; font-size: 26px; margin-top: 1px; }
  .offer-upgrade { left: 173px; top: 186px; width: 92px; height: 92px; }
  .offer-upgrade .big { font-weight: 700; font-size: 17px; }
  .offer-upgrade .small { font-size: 17px; margin-top: 1px; }
  .offer-commit { left: 286px; top: 234px; width: 108px; height: 108px; }
  .offer-commit .big { font-weight: 700; font-size: 28px; }
  .offer-commit .small { font-size: 14px; margin-top: 3px; }

  .cta-arrow { position: absolute; left: 370px; top: 405px; width: 130px; height: 70px; }

  .cta-ring { position: absolute; left: 378px; top: 556px; width: 426px; height: 90px;
    border-radius: 45px; background: rgba(255,255,255,0.5); }
  .cta { position: absolute; left: 388px; top: 566px; width: 408px; height: 70px; border-radius: 35px;
    background: linear-gradient(180deg, var(--red) 0%, var(--red-dark) 100%);
    color: var(--white); font-family: "Roboto Condensed", Arial, sans-serif; font-weight: 700;
    font-size: 33px; display: flex; align-items: center; justify-content: center; text-decoration: none; }

  .testimonial { position: absolute; left: 0; top: 674px; width: 1173px; text-align: center;
    font-size: 12.5px; line-height: 19px; color: var(--ink); }

  .contact-band { position: absolute; left: 0; top: 742px; width: 1200px; height: 83px; background: var(--band);
    display: flex; align-items: center; justify-content: center; gap: 6px; padding-right: 25px; }
  .contact-lead { font-size: 12px; margin-top: 8px; }
  .contact-phone { font-weight: 700; font-size: 30px; letter-spacing: 0.5px; }
</style>
</head>
<body>
  <header class="site-header">
    <div class="brand"><span class="brand-dot"></span>pingrova.net</div>
    <nav class="benefit-nav">
      <div class="benefit" style="left:573px">
        <svg viewBox="0 0 34 32" fill="none" stroke="#333" stroke-width="2"><rect x="7" y="5" width="24" height="14" rx="1"/><path d="M4 9v14h22"/><text x="19" y="15.5" font-size="9" text-anchor="middle" fill="#333" stroke="none" font-family="Arial">$</text></svg>
        Increase Revenue
      </div>
      <div class="benefit" style="left:778px">
        <svg viewBox="0 0 34 32" fill="none" stroke="#333" stroke-width="2"><path d="M17 3v24M9 28h16M5 8h24M6 8l-3 9h7zM28 8l-3 9h7z"/></svg>
        Lift Your Workload
      </div>
      <div class="benefit" style="left:979px">
        <svg viewBox="0 0 34 32" fill="none" stroke="#333" stroke-width="2"><path d="M23 16a10 10 0 1 1-10-10"/><path d="M13 11v6h5"/><circle cx="24" cy="8" r="6"/><text x="24" y="11" font-size="8" text-anchor="middle" fill="#333" stroke="none" font-family="Arial">$</text></svg>
        Save Time
      </div>
    </nav>
  </header>

  <section class="hero">
    <div class="hero-photo" role="img" aria-label="Photo of hands holding a smartphone showing a red chat bubble, blurred city lights behind"></div>

    <div class="offer offer-count"><span class="big">500</span><span class="small">messages</span></div>
    <div class="offer offer-keyword"><span class="big">Custom</span><span class="small">Keyword</span></div>
    <div class="offer offer-upgrade"><span class="big">Upgrade</span><span class="small">or cancel</span></div>
    <div class="offer offer-commit"><span class="big">No</span><span class="small">Commitments</span></div>

    <svg class="cta-arrow" viewBox="0 0 130 70" fill="none" stroke="#fff" stroke-width="3.5" stroke-linecap="round" stroke-linejoin="round">
      <path d="M6 16 C50 4, 100 12, 120 60"/>
      <path d="M104 52 L120 60 L123 42"/>
    </svg>
  </section>

  <div class="cta-ring"></div>
  <a class="cta" href="#">Try for $1</a>

  <p class="testimonial">“I switched suppliers &amp; now have Pingrova. Training, support, &amp; functionality are superb.<br>This will be a long term relationship.”</p>

  <footer class="contact-band">
    <span class="contact-lead">Questions? Give us a call.</span>
    <span class="contact-phone">1-877-555-0142</span>
  </footer>
</body>
</html>
```